Bright Path Medical Centers - website

Would like a multicultural website with pictures of physicians and nurses of all races interacting with patients of all races and ages from kids to seniors (in a medical practice) not a hospital.

Would like a page devoted to Pediatric Care, Adult/Family Care, Retirees/Senior Care. With a list of general primary care services for each page, including lab and transportation.
Updates

Target Market(s)

Adult medicine, Pediatric Medicine, Retiree/Senior Care

Industry/Entity Type

Health Care

Number of Pages Required

3 page

Font styles to use
Sans Serif

Requirements
Must have
• I like the website “oakridgefamilyclinic.example” in Atlanta.
• Prefer the design look and feel like this even though the services are very different.

```html
<!DOCTYPE html>
<html lang="en">
<head>
<meta charset="utf-8">
<title>Bright Path Medical Centers</title>
<link href="https://fonts.googleapis.com/css2?family=Poppins:wght@300;400;500;600&family=Open+Sans:wght@400;600&display=swap" rel="stylesheet">
<style>
:root{
  --blue:#1c6fc0;
  --blue-bright:#1e8fe0;
  --nav-top:#2a86d2;
  --nav-bottom:#1867b3;
  --text:#555b63;
  --dark:#333;
  --footer:#161c2a;
  --footer-text:#c9ccd3;
  --line:#d8d8d8;
  --white:#fff;
}
*{margin:0;padding:0;box-sizing:border-box}
html,body{width:930px;height:1200px;overflow:hidden;background:var(--white)}
body{position:relative;font-family:'Open Sans',sans-serif;color:var(--text)}
.site-header{position:absolute;left:0;top:0;width:930px;height:63px}
.brand{position:absolute;left:75px;top:19px;font-family:'Poppins',sans-serif;font-size:18px;font-weight:400;color:var(--blue);letter-spacing:.2px}
.brand b{font-weight:600}
.call{position:absolute;right:77px;top:21px;font-family:'Poppins',sans-serif;font-size:14px;font-weight:500;color:var(--blue);display:flex;align-items:center;gap:6px}
.main-nav{position:absolute;left:0;top:63px;width:930px;height:44px;background:linear-gradient(var(--nav-top),var(--nav-bottom))}
.main-nav ul{list-style:none;position:absolute;left:77px;top:0;display:flex;height:44px}
.main-nav li{height:44px;line-height:44px;font-family:'Poppins',sans-serif;font-size:12.5px;color:var(--white);padding:0 25px}
.main-nav li.active{background:var(--blue-bright);font-weight:600;padding:0 23px}
.hero{position:absolute;left:0;top:107px;width:930px;height:339px;background:linear-gradient(90deg,#d9a8c4 0%,#e9d8cf 20%,#6d7fb0 35%,#b44a7c 50%,#c8cbe0 62%,#3a2f33 72%,#aab8e2 88%,#c7d0ee 100%)}
.hero h1{position:absolute;left:0;width:930px;top:228px;text-align:center;font-family:'Poppins',sans-serif;font-size:23px;font-weight:600;color:var(--white);text-shadow:0 1px 3px rgba(0,0,0,.5)}
.btn{display:block;position:absolute;background:linear-gradient(#f2f2f2,#d8d8d8);border:1px solid #c8c8c8;font-family:'Open Sans',sans-serif;font-size:10.5px;color:#444;text-align:center}
.hero .btn{left:417px;top:267px;width:96px;height:23px;line-height:21px}
.welcome h2{position:absolute;left:0;width:930px;top:472px;text-align:center;font-family:'Poppins',sans-serif;font-size:17px;font-weight:600;color:var(--blue)}
.welcome .rule{position:absolute;left:441px;top:502px;width:48px;height:2px;background:var(--line)}
.welcome p{position:absolute;left:130px;width:670px;top:512px;text-align:center;font-size:10px;line-height:20px;color:var(--text)}
.welcome .btn{left:424px;top:654px;width:83px;height:23px;line-height:21px}
.subscribe{position:absolute;left:106px;top:718px;width:155px}
.subscribe h3{font-family:'Poppins',sans-serif;font-weight:400;font-size:22px;color:var(--blue)}
.subscribe p{margin-top:4px;font-family:'Poppins',sans-serif;font-size:11px;color:var(--dark)}
.email{position:absolute;left:-2px;top:66px;width:154px;height:24px;border:1px solid var(--line);font-size:10px;color:#333;padding:5px 9px;display:flex;justify-content:space-between;align-items:center}
.join{position:absolute;left:0;top:97px;width:76px;height:24px;background:var(--blue);color:var(--white);font-size:10.5px;text-align:center;line-height:24px}
.pager{position:absolute;left:0;top:144px;display:flex;gap:3px}
.pager span{width:18px;height:17px;background:#eee;display:flex;align-items:center;justify-content:center}
.pager span+span{background:#ddd}
.card{position:absolute;top:715px;width:170px;height:216px;border:1px solid #ddd}
.card .photo{height:120px}
.card h4{margin:9px 8px 0;font-family:'Poppins',sans-serif;font-weight:400;font-size:12.5px;color:var(--dark)}
.card p{margin:3px 8px 0;font-size:9.5px;line-height:16px;text-align:justify;color:var(--text)}
.footer{position:absolute;left:0;top:962px;width:930px;height:238px;background:var(--footer)}
.footer svg.curve{position:absolute;left:0;top:0}
.footer h5{position:absolute;top:53px;font-family:'Poppins',sans-serif;font-weight:400;font-size:16px;color:var(--blue-bright)}
.footer .f-brand{left:76px;font-size:15px}
.footer .f-brand b{font-weight:600}
.f-about{position:absolute;left:76px;top:99px;width:190px;font-size:9.5px;line-height:16px;color:var(--footer-text)}
.links{position:absolute;left:299px;top:91px;width:134px;list-style:none}
.links li{height:32px;line-height:26px;border-bottom:1px dashed #8a8e98;font-size:10.5px;color:var(--footer-text);padding-left:6px}
.links li::before{content:"›";margin-right:14px}
.t-arrows{position:absolute;left:604px;top:59px;display:flex;gap:2px}
.t-arrows span{width:13px;height:11px;background:#9a9ea6;color:#222;font-size:8px;line-height:11px;text-align:center}
.avatar{position:absolute;left:463px;top:82px;width:42px;height:42px;border-radius:50%;background:linear-gradient(#dfe3e8,#9aa3ad)}
.t-name{position:absolute;left:518px;top:85px;font-family:'Poppins',sans-serif;font-size:11px;color:var(--blue-bright)}
.t-role{position:absolute;left:518px;top:101px;font-size:9px;color:var(--blue-bright)}
.t-quote{position:absolute;left:461px;top:136px;width:180px;font-size:9.5px;line-height:16px;color:var(--footer-text)}
.contact-list{position:absolute;left:667px;top:89px;width:180px;list-style:none}
.contact-list li{display:flex;gap:6px;font-size:9.5px;line-height:16px;color:var(--footer-text);padding:2px 0 8px;margin-bottom:6px;border-bottom:1px dashed #8a8e98}
.contact-list li:last-child{border:none}
.bottom-bar{position:absolute;left:0;top:1166px;width:930px;height:34px;border-top:1px solid #2a3142;background:var(--footer);text-align:center;font-size:8.5px;line-height:32px;color:var(--footer-text)}
.to-top{position:absolute;left:819px;top:1164px;width:32px;height:24px;border-radius:12px;background:var(--blue-bright);display:flex;align-items:center;justify-content:center}
</style>
</head>
<body>
<header class="site-header">
  <div class="brand">BRIGHT PATH <b>MEDICAL</b></div>
  <div class="call">
    <svg width="13" height="13" viewBox="0 0 24 24"><path fill="#1c6fc0" d="M6.6 10.8a15 15 0 006.6 6.6l2.2-2.2c.3-.3.7-.4 1-.2 1.1.4 2.3.6 3.6.6.6 0 1 .4 1 1V20c0 .6-.4 1-1 1A17 17 0 013 4c0-.6.4-1 1-1h3.5c.6 0 1 .4 1 1 0 1.3.2 2.5.6 3.6.1.3 0 .7-.2 1z"/></svg>
    Call Us : 1-800 555 0142
  </div>
</header>
<nav class="main-nav">
  <ul>
    <li class="active">Home</li>
    <li>About Us</li>
    <li>Paediatric Care</li>
    <li>Adult/Family Care</li>
    <li>Retirees/Senior Care</li>
    <li>Contact us</li>
  </ul>
</nav>
<section class="hero" role="img" aria-label="Group of smiling physicians and nurses from diverse backgrounds standing together">
  <h1>BRIGHT PATH MEDICAL CENTERS</h1>
  <span class="btn">LEARN MORE</span>
</section>
<section class="welcome">
  <h2>WELCOME</h2>
  <div class="rule"></div>
  <p>Sed ut perspiciatis unde omnis iste natus error sit voluptatem accusantium doloremque laudantium, totam rem aperiam, eaque ipsa quae ab illo inventore veritatis et quasi architecto beatae vitae dicta sunt explicabo. Nemo enim ipsam voluptatem quia voluptas sit aspernatur aut odit aut fugit, sed quia consequuntur magni dolores eos qui ratione voluptatem sequi nesciunt. Neque porro quisquam est, qui dolorem ipsum quia dolor sit amet, consectetur, adipisci velit, sed quia non numquam eius modi tempora incidunt ut labore et dolore magnam aliquam quaerat voluptatem. Ut enim ad minima veniam, quis nostrum exercitationem ullam corporis suscipit laboriosam, nisi ut aliquid ex ea commodi consequatur? Quis autem vel eum iure reprehenderit qui in ea voluptate velit</p>
  <span class="btn">READ MORE</span>
</section>
<aside class="subscribe">
  <h3>Subscribe</h3>
  <p>Join with our Newsletter</p>
  <div class="email">Enter Email id
    <svg width="10" height="8" viewBox="0 0 10 8"><rect x=".5" y=".5" width="9" height="7" fill="none" stroke="#333"/><path d="M.5 .5L5 4.5 9.5 .5" fill="none" stroke="#333"/></svg>
  </div>
  <div class="join">JOIN NOW</div>
  <div class="pager">
    <span><svg width="6" height="8" viewBox="0 0 6 8"><path d="M4.5 1L1.5 4l3 3" fill="none" stroke="#333"/></svg></span>
    <span><svg width="6" height="8" viewBox="0 0 6 8"><path d="M1.5 1l3 3-3 3" fill="none" stroke="#333"/></svg></span>
  </div>
</aside>
<article class="card" style="left:287px">
  <div class="photo" role="img" aria-label="Woman playing with a smiling young child in a clinic" style="background:linear-gradient(135deg,#f2ece6,#c9644a 55%,#2f2a2a)"></div>
  <h4>Paediatric Care</h4>
  <p>Neque porro quisquam est, qui dolorem ipsum quia dolor sit amet, consectetur,</p>
</article>
<article class="card" style="left:473px">
  <div class="photo" role="img" aria-label="Doctor talking with a patient resting in bed" style="background:linear-gradient(135deg,#e6eaec,#c7d3da 50%,#8ea1b2)"></div>
  <h4>Adult/Family Care</h4>
  <p>Neque porro quisquam est, qui dolorem ipsum quia dolor sit amet, consectetur,</p>
</article>
<article class="card" style="left:658px">
  <div class="photo" role="img" aria-label="Caregiver holding hands with an elderly woman" style="background:linear-gradient(135deg,#dcdcdc,#c06a6a 45%,#e8ecef)"></div>
  <h4>Retirees/Senior Care</h4>
  <p>Neque porro quisquam est, qui dolorem ipsum quia dolor sit amet, consectetur,</p>
</article>
<footer class="footer">
  <svg class="curve" width="930" height="30" viewBox="0 0 930 30"><path d="M0 0H930V6Q465 -2 0 6Z" fill="#fff"/><path d="M0 6Q465 30 930 6V0H0Z" fill="#fff"/></svg>
  <h5 class="f-brand">BRIGHT PATH <b>MEDICAL</b></h5>
  <p class="f-about">Sed ut perspiciatis unde omnis iste natus error sit voluptatem accusantium doloremque laudantium, totam rem aperiam, eaque ipsa quae ab illo inventore veritatis et</p>
  <h5 style="left:301px">Usefull Links</h5>
  <ul class="links"><li>Privacy Policy</li><li>Terms &amp; Condictions</li><li>Sitemap</li></ul>
  <h5 style="left:461px">Testimonials</h5>
  <div class="t-arrows"><span>‹</span><span>›</span></div>
  <div class="avatar" role="img" aria-label="Client portrait"></div>
  <div class="t-name">Marcus Lindqvist</div>
  <div class="t-role">CEO</div>
  <p class="t-quote">Lorem ipsum dolor sit amet, consectetur adipiscing elit, sed do eiusmod tempor incididunt ut labore et...</p>
  <h5 style="left:667px">Contact</h5>
  <ul class="contact-list">
    <li><svg width="9" height="12" viewBox="0 0 9 12"><path d="M4.5 0A4.5 4.5 0 000 4.5C0 8 4.5 12 4.5 12S9 8 9 4.5A4.5 4.5 0 004.5 0zm0 6.2a1.7 1.7 0 110-3.4 1.7 1.7 0 010 3.4z" fill="#8a8e98"/></svg><span>48 Maple Court, Suite 2, Riverton, USA, 30012.</span></li>
    <li><svg width="11" height="11" viewBox="0 0 24 24"><path fill="#8a8e98" d="M6.6 10.8a15 15 0 006.6 6.6l2.2-2.2c.3-.3.7-.4 1-.2 1.1.4 2.3.6 3.6.6.6 0 1 .4 1 1V20c0 .6-.4 1-1 1A17 17 0 013 4c0-.6.4-1 1-1h3.5c.6 0 1 .4 1 1 0 1.3.2 2.5.6 3.6.1.3 0 .7-.2 1z"/></svg><span>+ 1 (404) 555 0178</span></li>
    <li><svg width="12" height="10" viewBox="0 0 12 10"><rect x=".5" y=".5" width="11" height="9" fill="none" stroke="#8a8e98"/><path d="M.5 .5L6 5l5.5-4.5" fill="none" stroke="#8a8e98"/></svg><span>hello@brightpathmed.example</span></li>
  </ul>
</footer>
<div class="bottom-bar">Copyright © 2017 www.brightpathmed.example &nbsp;|&nbsp; All Rights Reserved.</div>
<div class="to-top"><svg width="12" height="8" viewBox="0 0 12 8"><path d="M1 7l5-5 5 5" fill="none" stroke="#fff" stroke-width="1.6"/></svg></div>
</body>
</html>
```